Anzeigengestaltung für Steuerberatung
Zielgruppe
Steuerberatung, Zielgruppe: Unternehmen und Privatpersonen
Aufgabenstellung
Logo, Anschrift mit vollständigem Namen, Stichwörter: nahbar.ehrlich.weise begleitet.
Farbe wie Logo auf der Website. Anbei die Farbcodes C32 M38 Y37 K15
Anzeige soll frisch, ansprechend, jung, klare Informationen ohne verspielte Details. Trotzdem im Stil des bisherigen bewegen.
Anzeigengröße: 9,00 x 6,50 cm

```html
<!DOCTYPE html>
<html lang="de">
<head>
<meta charset="utf-8">
<title>Lenhardt Steuerberatung – Anzeige</title>
<link href="https://fonts.googleapis.com/css2?family=Montserrat:wght@500;600&family=Roboto+Condensed:wght@700&family=Roboto:wght@400;500&display=swap" rel="stylesheet">
<style>
  :root {
    --taupe: #978480;
    --taupe-dark: #7d6b67;
    --brand-text: #8a7470;
    --ink: #0b0b0b;
    --white: #ffffff;
    --stripe: #d8d8da;
    --stage: #ececec;
  }
  html, body {
    margin: 0;
    width: 1200px;
    height: 1117px;
    overflow: hidden;
    background: var(--stage);
  }
  .ad {
    position: absolute;
    left: 40px;
    top: 155px;
    width: 1120px;
    height: 806px;
    background: var(--white);
    overflow: hidden;
    box-shadow: 0 2px 8px rgba(0,0,0,.15);
  }
  .ad-shapes {
    position: absolute;
    inset: 0;
    width: 100%;
    height: 100%;
  }
  .brand {
    position: absolute;
    left: 40px;
    width: 400px;
    top: 82px;
    text-align: center;
    color: var(--brand-text);
    font-family: "Montserrat", sans-serif;
  }
  .brand-dot {
    width: 110px;
    height: 110px;
    margin: 0 auto 26px;
    border-radius: 50%;
    border: 3px solid var(--brand-text);
    box-sizing: border-box;
  }
  .brand-name {
    font-size: 30px;
    font-weight: 500;
    letter-spacing: 3px;
    line-height: 1;
    white-space: nowrap;
  }
  .brand-sub {
    display: flex;
    align-items: center;
    justify-content: center;
    gap: 8px;
    margin-top: 10px;
    font-size: 16px;
    font-weight: 600;
    letter-spacing: 2px;
  }
  .brand-sub::before, .brand-sub::after {
    content: "";
    width: 46px;
    height: 2px;
    background: var(--brand-text);
  }
  .headline {
    position: absolute;
    left: 78px;
    top: 320px;
    margin: 0;
    color: var(--white);
    font-family: "Roboto Condensed", sans-serif;
    font-weight: 700;
    font-size: 62px;
    line-height: 78px;
    text-transform: uppercase;
    text-shadow: 2px 2px 2px rgba(0,0,0,.25);
  }
  .contact {
    position: absolute;
    left: 78px;
    top: 598px;
    color: var(--white);
    font-family: "Roboto", sans-serif;
  }
  .contact-phone {
    display: flex;
    align-items: center;
    gap: 14px;
    font-size: 46px;
    font-weight: 500;
    line-height: 1;
    margin-bottom: 12px;
  }
  .contact-line {
    display: flex;
    align-items: center;
    gap: 22px;
    font-size: 26px;
    line-height: 36px;
    margin-left: 3px;
  }
  .contact-icon {
    width: 18px;
    height: 18px;
    flex: none;
  }
</style>
</head>
<body>
  <div class="ad">
    <svg class="ad-shapes" viewBox="0 0 1672 1204" preserveAspectRatio="none">
      <defs>
        <linearGradient id="photoBase" x1="0" y1="0" x2="1" y2="1">
          <stop offset="0" stop-color="#4d5a57"/>
          <stop offset=".5" stop-color="#6b6460"/>
          <stop offset="1" stop-color="#b9b2aa"/>
        </linearGradient>
        <radialGradient id="toneWindow"><stop offset="0" stop-color="#7f8f8c" stop-opacity=".8"/><stop offset="1" stop-color="#7f8f8c" stop-opacity="0"/></radialGradient>
        <radialGradient id="toneWarm"><stop offset="0" stop-color="#8a6a55" stop-opacity=".85"/><stop offset="1" stop-color="#8a6a55" stop-opacity="0"/></radialGradient>
        <radialGradient id="toneBlazer"><stop offset="0" stop-color="#d2ab9c" stop-opacity=".95"/><stop offset="1" stop-color="#d2ab9c" stop-opacity="0"/></radialGradient>
        <radialGradient id="toneChair"><stop offset="0" stop-color="#23262c" stop-opacity=".9"/><stop offset="1" stop-color="#23262c" stop-opacity="0"/></radialGradient>
        <radialGradient id="toneSuit"><stop offset="0" stop-color="#d9d5cf" stop-opacity=".95"/><stop offset="1" stop-color="#d9d5cf" stop-opacity="0"/></radialGradient>
        <radialGradient id="toneGrey"><stop offset="0" stop-color="#a9a39c" stop-opacity=".8"/><stop offset="1" stop-color="#a9a39c" stop-opacity="0"/></radialGradient>
        <clipPath id="photoClip"><polygon points="577,0 1672,0 1672,1204 984,1204"/></clipPath>
      </defs>
      <rect class="contact-band" x="0" y="639" width="1000" height="565" fill="var(--ink)"/>
      <polygon class="accent-stripe" points="542,0 580,0 986,1204 950,1204" fill="var(--stripe)"/>
      <g class="photo" role="img" aria-label="Foto: Steuerberaterin im Beratungsgespräch mit einem Mandanten im Büro" clip-path="url(#photoClip)">
        <rect x="560" y="0" width="1112" height="1204" fill="url(#photoBase)"/>
        <ellipse cx="760" cy="120" rx="380" ry="260" fill="url(#toneWindow)"/>
        <ellipse cx="960" cy="330" rx="330" ry="360" fill="url(#toneWarm)"/>
        <ellipse cx="1060" cy="780" rx="340" ry="380" fill="url(#toneBlazer)"/>
        <ellipse cx="1350" cy="600" rx="230" ry="330" fill="url(#toneChair)"/>
        <ellipse cx="1540" cy="220" rx="260" ry="260" fill="url(#toneGrey)"/>
        <ellipse cx="1520" cy="900" rx="300" ry="420" fill="url(#toneSuit)"/>
        <ellipse cx="1200" cy="1130" rx="320" ry="140" fill="url(#toneWarm)"/>
      </g>
      <polygon class="headline-fold" points="800,842 902,842 915,872 800,842" fill="var(--taupe-dark)"/>
      <polygon class="headline-box" points="57,437 777,437 902,842 57,842" fill="var(--taupe)"/>
      <polygon class="headline-edge" points="777,437 790,437 912,842 902,842" fill="var(--taupe-dark)"/>
    </svg>

    <div class="brand">
      <div class="brand-dot"></div>
      <div class="brand-name">MARIE LENHARDT</div>
      <div class="brand-sub">STEUERBERATUNG</div>
    </div>

    <h1 class="headline">Nahbar.<br>Ehrlich.<br>Weise begleitet.</h1>

    <div class="contact">
      <div class="contact-phone">
        <svg class="contact-icon" style="width:28px;height:34px" viewBox="0 0 24 28"><path d="M6 1c1 0 2 .5 2.5 1.5l2 4.5c.4 1 0 2-.7 2.6L8 11c1 3 3 6 5.5 8l1.5-1.6c.7-.7 1.8-.9 2.7-.4l4.2 2.3c1 .5 1.4 1.6 1.1 2.6l-1 2.8C21.5 26 20 27 18.5 27 9 25 2 16 1.5 5.5 1.5 3 3 1 6 1z" fill="var(--taupe)"/></svg>
        <span>07123 / 4567890</span>
      </div>
      <div class="contact-line">
        <svg class="contact-icon" viewBox="0 0 20 20"><circle cx="10" cy="10" r="10" fill="var(--taupe)"/><rect x="5" y="6.5" width="10" height="7" fill="none" stroke="#fff" stroke-width="1.3"/><path d="M5 6.5l5 4 5-4" fill="none" stroke="#fff" stroke-width="1.3"/></svg>
        <span>kontakt@lenhardt-steuerberatung.de</span>
      </div>
      <div class="contact-line">
        <svg class="contact-icon" viewBox="0 0 20 24"><path d="M10 0a9 9 0 0 1 9 9c0 6-9 15-9 15S1 15 1 9a9 9 0 0 1 9-9z" fill="var(--taupe)"/><circle cx="10" cy="9" r="3.2" fill="var(--ink)"/></svg>
        <span>Lindenweg 12, 72500 Musterstadt</span>
      </div>
      <div class="contact-line">
        <svg class="contact-icon" viewBox="0 0 20 20"><circle cx="10" cy="10" r="10" fill="var(--taupe)"/><g fill="none" stroke="#fff" stroke-width="1.1"><circle cx="10" cy="10" r="5.5"/><ellipse cx="10" cy="10" rx="2.4" ry="5.5"/><path d="M4.5 10h11"/></g></svg>
        <span>www.lenhardt-steuerberatung.de</span>
      </div>
    </div>
  </div>
</body>
</html>
```